Brightbay Business Card Design

Our company is called Brightbay. We manufacture confectionary snacks & frozen novelties. Our initial product portfolio includes frozen ice lollies/popsicles & stick ice cream bars.

We require a business card design.

Please use the attached Logo.

Please use an orange, brown, yellow colour code. You may choose any combination of the 3 or include all three. The logo however must remain orange.

Target Market(s)

Business card will be targeted at distributors of our products such as supermarket procurement managers, convenience store owners, wholesale distributors and merchandising agents.

Industry/Entity Type

Business

Requirements
Must have
• Calvin Obeng_Director/ P.O.Box Dunmore 5172, Accra, Ghana / m: 00233(0)507318924/ e: calvin.obeng@mailvora.co.uk

```html
<!DOCTYPE html>
<html lang="en">
<head>
<meta charset="utf-8">
<title>Brightbay Business Card</title>
<link rel="stylesheet" href="https://fonts.googleapis.com/css2?family=Exo+2:wght@400;600;800&display=swap">
<style>
  :root {
    --page-bg: #eceef1;
    --card-black: #0b0604;
    --card-brown: #3a1d0e;
    --brand-orange: #f07324;
    --text-white: #f7f2ee;
  }
  * { box-sizing: border-box; margin: 0; padding: 0; }
  html, body {
    width: 1200px;
    height: 1000px;
    overflow: hidden;
    background: var(--page-bg);
    font-family: "Exo 2", sans-serif;
  }
  .canvas {
    position: relative;
    width: 1200px;
    height: 1000px;
  }
  .business-card {
    position: absolute;
    left: 100px;
    top: 214px;
    width: 1000px;
    height: 572px;
    overflow: hidden;
    background:
      radial-gradient(ellipse 520px 420px at 560px 300px, var(--card-brown) 0%, rgba(58,29,14,0.55) 45%, rgba(11,6,4,0) 80%),
      var(--card-black);
    box-shadow: 0 6px 18px rgba(0,0,0,0.18);
  }
  .brand-name {
    position: absolute;
    left: 330px;
    top: 80px;
    width: 620px;
    font-weight: 800;
    font-size: 118px;
    line-height: 1;
    letter-spacing: -1px;
    white-space: nowrap;
    color: var(--brand-orange);
  }
  .person {
    position: absolute;
    left: 82px;
    top: 300px;
  }
  .person-name {
    font-weight: 600;
    font-size: 42px;
    color: var(--text-white);
    line-height: 1.1;
  }
  .person-title {
    margin-top: 18px;
    font-weight: 400;
    font-size: 42px;
    color: var(--brand-orange);
    line-height: 1.1;
  }
  .contact-list {
    position: absolute;
    left: 320px;
    top: 362px;
    list-style: none;
  }
  .contact-item {
    display: flex;
    align-items: baseline;
    gap: 14px;
    height: 66px;
    font-size: 26px;
    white-space: nowrap;
  }
  .contact-label {
    flex: 0 0 104px;
    color: var(--brand-orange);
    text-align: right;
  }
  .contact-value {
    color: var(--text-white);
  }
</style>
</head>
<body>
<main class="canvas">
  <section class="business-card">
    <h1 class="brand-name">Brightbay</h1>
    <div class="person">
      <p class="person-name">Calvin Obeng</p>
      <p class="person-title">Director</p>
    </div>
    <ul class="contact-list">
      <li class="contact-item"><span class="contact-label">Address</span><span class="contact-value">P.O.Box Dunmore 5172, Accra, Ghana</span></li>
      <li class="contact-item"><span class="contact-label">Phone</span><span class="contact-value">00233(0)507318924</span></li>
      <li class="contact-item"><span class="contact-label">Email</span><span class="contact-value">calvin.obeng@mailvora.co.uk</span></li>
    </ul>
  </section>
</main>
</body>
</html>
```